Pilates Classes Flyer Design

I need a flyer designed that will promote my range of classes held in Bath, UK. I teach beginners, intermediate level and Over 50's and 60's and also teach individuals in their own homes. I would like to see designs using my colours blue Pantone 306 and Lime Green 14-0452 TPX TCX. The flyer should reflect a friendly, welcoming and professional class structure. I attach an old flyer for your reference and copy.

Target Market(s)

Men and Women who have busy lives working hard, who recognise they need to stretch out, do some exercise and de-stress after a busy day

Ladies over 50 who want to do some Pilates in a friendly fun environment and meet people at the same time.

Industry/Entity Type

It Professional

Font styles to use
Sans Serif
Script

Requirements
Must have
• One-sided flyer
Text only logo. Drop the figure

```html
<!DOCTYPE html>
<html lang="en">
<head>
<meta charset="utf-8">
<title>Stillpoint Pilates – Class Flyer</title>
<link rel="stylesheet" href="https://fonts.googleapis.com/css2?family=Bebas+Neue&family=Lato:wght@300;400;700&display=swap">
<style>
  :root{
    --page:#e9ecee;
    --blue-light:#5cc7ec;
    --blue:#3aa6cf;
    --blue-deep:#17799f;
    --navy:#0f6a8c;
    --lime:#cfdd6a;
    --ink:#1f262b;
    --white:#ffffff;
    --red:#e8222b;
    --badge:#222222;
    --sky-top:#8fa8d8;
    --sky-bottom:#c4d3ea;
    --logo:#6cc3de;
  }
  *{box-sizing:border-box;margin:0;padding:0}
  html,body{width:1200px;height:900px;overflow:hidden;background:var(--page)}
  .canvas{position:relative;width:1200px;height:900px;overflow:hidden}
  .flyer{
    position:absolute;left:28px;top:46px;width:1040px;height:735px;
    transform:scale(1.1);transform-origin:0 0;overflow:hidden;
    background:linear-gradient(180deg,var(--blue-light) 0%,var(--blue) 45%,var(--blue-deep) 100%);
    font-family:"Lato",Arial,sans-serif;
    box-shadow:0 6px 18px rgba(0,0,0,.18);
  }
  .flyer__shapes{position:absolute;inset:0;width:1040px;height:735px}
  .email{position:absolute;right:34px;top:26px;color:var(--white);font-family:Arial,Helvetica,sans-serif;font-weight:700;font-size:17px}
  .about{position:absolute;left:70px;top:238px}
  .about__title{color:var(--white);font-family:Arial,Helvetica,sans-serif;font-weight:700;font-size:24px;margin-bottom:12px}
  .about__text{color:var(--ink);font-family:Arial,Helvetica,sans-serif;font-size:17px;line-height:24px}
  .badge{
    position:absolute;left:555px;top:240px;width:180px;height:180px;border-radius:50%;
    background:var(--badge);border:6px solid var(--white);
    display:flex;flex-direction:column;align-items:center;justify-content:center;
    font-family:"Bebas Neue",Impact,sans-serif;line-height:.92;text-align:center;
  }
  .badge__big{color:var(--red);font-size:50px}
  .badge__red{color:var(--red);font-size:28px}
  .badge__white{color:var(--white);font-size:27px}
  .call{position:absolute;left:750px;top:358px;font-family:"Bebas Neue",Impact,sans-serif;line-height:.95}
  .call__label{color:var(--white);font-size:56px}
  .call__number{color:var(--ink);font-size:62px;letter-spacing:1px}
  .headline{position:absolute;left:70px;top:396px;color:var(--ink);font-family:"Bebas Neue",Impact,sans-serif;font-size:62px;line-height:1}
  .subline{position:absolute;left:70px;top:455px;color:var(--lime);font-size:20px;line-height:27px}
  .levels{
    position:absolute;left:48px;top:537px;width:570px;height:44px;border-radius:22px;background:var(--white);
    color:var(--red);font-family:"Bebas Neue",Impact,sans-serif;font-size:25px;
    display:flex;align-items:center;justify-content:center;
  }
  .venues{position:absolute;left:70px;top:600px;font-size:17px;line-height:24px}
  .venues__name{color:var(--ink);font-weight:700}
  .venues__time{color:var(--lime)}
  .brand{position:absolute;left:790px;top:600px;display:flex;align-items:center;gap:12px}
  .brand__dot{width:18px;height:18px;border-radius:50%;background:var(--logo)}
  .brand__name{color:var(--logo);font-family:"Lato",Arial,sans-serif;font-weight:300;font-size:34px;line-height:1}
</style>
</head>
<body>
<div class="canvas">
  <article class="flyer">
    <svg class="flyer__shapes" viewBox="0 0 1040 735" aria-hidden="false">
      <defs>
        <linearGradient id="sky" x1="0" y1="0" x2="0" y2="1">
          <stop offset="0" stop-color="var(--sky-top)"/>
          <stop offset="1" stop-color="var(--sky-bottom)"/>
        </linearGradient>
      </defs>
      <!-- lime frame around the photo -->
      <path d="M200,0 C90,40 40,120 70,170 C140,250 500,240 620,245 C800,250 900,255 1040,230 L1040,320 C900,300 800,305 720,310 C600,300 220,260 110,170 C60,110 110,30 200,0 Z" fill="var(--lime)"/>
      <!-- photo area -->
      <path role="img" aria-label="Photo of a woman stretching her arm out against a bright blue sky" d="M245,0 L1040,0 L1040,290 C900,282 800,292 725,300 C600,290 220,255 125,170 C80,115 140,35 245,0 Z" fill="url(#sky)"/>
      <!-- left swooshes -->
      <path d="M0,318 C120,335 260,352 360,354 C260,362 120,372 0,402 Z" fill="var(--navy)"/>
      <path d="M0,328 C120,342 250,352 340,355 C250,360 120,368 0,390 Z" fill="var(--lime)"/>
      <path d="M480,392 C520,375 550,362 600,348 L605,360 C560,372 520,384 480,392 Z" fill="var(--lime)"/>
      <!-- bottom-right white panel -->
      <path d="M560,735 C700,640 880,520 1040,490 L1040,525 C880,560 740,650 640,735 Z" fill="var(--lime)"/>
      <path d="M640,735 C740,650 880,560 1040,525 L1040,735 Z" fill="var(--white)"/>
    </svg>

    <p class="email">helen.ashdown@example.co.uk</p>

    <section class="about">
      <h2 class="about__title">ABOUT US</h2>
      <p class="about__text">Quality teaching with Balanced Form Method Teacher.<br>Progressive approach. Teaching good movement skills.</p>
    </section>

    <div class="badge">
      <span class="badge__big">SMALL</span>
      <span class="badge__red">CLASS SIZES</span>
      <span class="badge__white">AND FRIENDLY</span>
      <span class="badge__white">ATMOSPHERE</span>
    </div>

    <div class="call">
      <p class="call__label">CALL HELEN ON</p>
      <p class="call__number">07700900461</p>
    </div>

    <h1 class="headline">PILATES IS FOR EVERYONE</h1>
    <p class="subline">whatever level of fitness, age or ability to help<br>you build strength, flexibility and overall well-being</p>

    <p class="levels">BEGINNERS, INTERMEDIATE AND OVER 50’S CLASSES TO CHOOSE FROM</p>

    <div class="venues">
      <p class="venues__name">St Anne’s Church Hall, Elm Row</p>
      <p class="venues__time">Monday evenings, Tuesday and Friday mornings.</p>
      <p class="venues__time">Brookside Dr. Surgery Tuesday evenings.</p>
      <p class="venues__name">Harrow Centre, Mill Road,</p>
      <p class="venues__time">Wednesday mornings and evenings.</p>
    </div>

    <div class="brand">
      <span class="brand__dot"></span>
      <span class="brand__name">Stillpoint Pilates</span>
    </div>
  </article>
</div>
</body>
</html>
```